Wellness product startup company needs packing design

We are starting up with a range of wellness products and looking for colorful, modern & trendy designs, highlighting the brand and product name as bold & prominent as possible.
sending few samples which I tried to design myself. not at all happy with the result though.
Also please use colors that go well with the Health & Wellness products (these products also comes under food supplement range)
Target Market(s)
India
Industry/Entity Type
Health And Wellness
Font styles to use
Serif
Colors
9bcb3b
f37122
e34197
Requirements
Must have
- Prominent logo & product name
Nice to have
- I leave it to you.
Should not have
- I leave it to designer.

```html
<!DOCTYPE html>
<html lang="en">
<head>
<meta charset="utf-8">
<title>Vita-Core Label</title>
<link href="https://fonts.googleapis.com/css2?family=Roboto+Condensed:wght@400;700;900&family=Oswald:wght@500;700&family=Satisfy&display=swap" rel="stylesheet">
<style>
:root{
  --lime:#9bc23c;
  --lime-dark:#6f9a1c;
  --maroon:#5c0e0e;
  --brown:#b27852;
  --ink:#1d1d1d;
  --white:#ffffff;
  --page:#e6e6e6;
}
*{box-sizing:border-box;margin:0;padding:0}
html,body{width:1200px;height:1200px;overflow:hidden;background:var(--page);font-family:"Roboto Condensed",sans-serif;color:var(--ink)}
.label{position:absolute;left:22px;top:371px;width:1156px;height:458px;background:var(--lime);overflow:hidden}
.panel{position:absolute;top:0;height:458px}
.panel-left{left:0;width:376px}
.panel-front{left:376px;width:404px;background:var(--white)}
.panel-right{left:780px;width:376px}
.info-box{position:absolute;top:30px;bottom:20px;background:var(--white);border:3px solid var(--maroon);padding:4px}
.panel-left .info-box{left:8px;right:8px}
.panel-right .info-box{left:12px;right:4px;padding:5px 6px}

/* nutrition */
.facts{display:flex;gap:3px;height:212px}
.facts-main,.facts-side{flex:1;font-size:6.2px;line-height:1.2}
.facts-title{font-weight:900;font-size:16px;border-bottom:3px solid var(--ink);line-height:1.05}
.facts table{width:100%;border-collapse:collapse}
.facts td{border-bottom:0.5px solid #777;padding:0 1px;white-space:nowrap;line-height:8.3px}
.facts-main td{line-height:8.6px}
.facts .group{background:var(--maroon);color:var(--white);font-weight:700}
.serving{margin:3px 0 6px;font-size:6.4px;line-height:1.3}
.use{font-size:6.4px;line-height:1.25;margin-top:3px}
.ingredients{background:var(--maroon);color:var(--white);font-size:8.4px;line-height:1.3;padding:4px 5px;margin-top:4px;text-align:justify}
.ingredients p+p{margin-top:6px}
.small-caps{font-size:6.6px;font-weight:700;margin-top:6px;line-height:1.3}
.maker{display:flex;gap:6px;margin-top:4px;font-size:8.4px;line-height:1.3}
.note{border:1px solid var(--ink);padding:1px 4px;font-size:8.4px;width:74px;flex:none;text-align:center}
.dist{font-size:6.6px;font-weight:700;margin-top:8px}

/* front */
.front-art{position:absolute;inset:0}
.brand{position:absolute;left:0;right:0;top:38px;text-align:center;font-family:"Roboto Condensed",sans-serif;font-weight:700;font-size:36px;color:var(--maroon);letter-spacing:1px}
.tagline{position:absolute;left:0;right:0;top:86px;text-align:center;font-size:14px;color:var(--ink)}
.product{position:absolute;left:0;right:0;top:186px;text-align:center;font-family:"Oswald",sans-serif;font-weight:700;font-size:68px;line-height:1;color:var(--maroon);letter-spacing:-1px}
.subtitle{position:absolute;left:0;right:0;top:262px;text-align:center;font-family:"Satisfy",cursive;font-size:19px;color:var(--maroon)}
.splash{position:absolute;left:110px;top:300px;width:190px;height:110px;border-radius:50% 50% 45% 45%;background:radial-gradient(ellipse at 50% 60%,#3d1f12 0%,#7b4a33 45%,rgba(178,120,82,0) 75%)}
.badge{position:absolute;left:302px;top:330px;width:92px;height:92px;border-radius:50%;background:var(--maroon);border:3px solid var(--white);box-shadow:0 0 0 2px var(--maroon);color:var(--white);font-size:6.5px;font-weight:700;text-align:center;display:flex;flex-direction:column;align-items:center;justify-content:center;gap:2px}
.badge-art{display:block;width:44px;height:28px;border-radius:50%;background:radial-gradient(circle,#8a3b1d,#4d1a0c)}
.badge-art-wrap{background:var(--white);border-radius:50%;padding:3px 4px}
.weight{position:absolute;left:0;right:0;top:424px;text-align:center;font-size:17px;font-weight:700;color:var(--maroon)}

/* right */
.headline{font-family:"Oswald",sans-serif;font-weight:700;font-size:14.5px;line-height:1.25;color:var(--maroon);text-align:center;margin-bottom:6px}
.copy{font-size:6.9px;line-height:1.25;text-align:justify}
.copy p{margin-bottom:3px}
.copy ul{padding-left:10px;margin-bottom:3px}
.copy li{margin-bottom:3px}
.protein{background:var(--maroon);color:var(--white);font-size:7px;line-height:1.5;padding:2px 4px;margin:3px 0}
.pdcaas{border:0.5px solid var(--ink);font-size:5.6px;padding:1px 3px;line-height:1.25}
.foot{display:flex;gap:8px;margin-top:4px}
.storage{flex:1.6;font-size:7.6px;line-height:1.3}
.storage strong{font-family:"Oswald",sans-serif;font-weight:500;font-size:10px;display:block;line-height:1.25}
.storage .best{font-family:"Oswald",sans-serif;font-weight:700;font-size:10.5px;margin-top:3px;display:block;white-space:nowrap}
.storage .fine{font-size:5px;white-space:nowrap}
.marketer{flex:1;font-size:6px;line-height:1.35}
.marketer .m-name{display:flex;align-items:center;gap:4px;font-weight:700;font-size:12px;color:var(--maroon);margin:3px 0}
.marketer .m-dot{width:10px;height:10px;border-radius:50%;background:var(--lime-dark)}
</style>
</head>
<body>
<div class="label">

  <section class="panel panel-left">
    <div class="info-box">
      <div class="facts">
        <div class="facts-main">
          <div class="facts-title">Nutrition Facts</div>
          <div class="serving"><b>Serving size</b> : 2 Table Spoons (25g approx)<br><b>Servings</b> : 2 Per day (1 for child 2-6 years)<br><b>Servings per container</b> : Approx 8</div>
          <table>
            <tr><td>Approx. Composition</td><td>Unit</td><td>Per100g</td><td>Per 25g</td></tr>
            <tr><td>Energy</td><td>K.cal</td><td>406</td><td>102</td></tr>
            <tr><td>Protein</td><td>g</td><td>20.5</td><td>5</td></tr>
            <tr><td>Fat</td><td>g</td><td>8.0</td><td>2</td></tr>
            <tr><td>&nbsp;Saturated fatty acid</td><td>g</td><td>4</td><td>1</td></tr>
            <tr><td>&nbsp;Mono unsaturated fatty acid</td><td>g</td><td>3.1</td><td>0.8</td></tr>
            <tr><td>&nbsp;Poly-unsaturated fatty acid</td><td>g</td><td>0.8</td><td>0.2</td></tr>
            <tr><td>&nbsp;Trans fatty acid</td><td>g</td><td>0</td><td>0</td></tr>
            <tr><td>&nbsp;Cholesterol</td><td>g</td><td>0</td><td>0</td></tr>
            <tr><td>Carbohydrate</td><td>g</td><td>63.0</td><td>16</td></tr>
            <tr><td>Lactose</td><td>g</td><td>0.0</td><td>0</td></tr>
          </table>
          <p class="use"><b>SUGGESTED USE:</b> Add 2 Table spoons (approx 25g) in a glass and mix with a little milk or water. Stir to form a smooth paste. Add more milk or water as desired and shake vigorously in a container for a frothy, delicious and nutritious drink. Sweeteners may be added, if desired.</p>
        </div>
        <div class="facts-side">
          <table>
            <tr class="group"><td colspan="4">10 Essential Minerals</td></tr>
            <tr><td>Calcium</td><td>mg</td><td>900</td><td>225</td></tr>
            <tr><td>Phosphorus</td><td>mg</td><td>750</td><td>187.5</td></tr>
            <tr><td>Iodine</td><td>mcg</td><td>75</td><td>18.8</td></tr>
            <tr><td>Magnesium</td><td>mg</td><td>80</td><td>20</td></tr>
            <tr><td>Iron</td><td>mg</td><td>10</td><td>2.5</td></tr>
            <tr><td>Zinc</td><td>mg</td><td>4.0</td><td>1.0</td></tr>
            <tr><td>Copper</td><td>mg</td><td>3</td><td>0.75</td></tr>
            <tr><td>Sodium</td><td>mg</td><td>400</td><td>100</td></tr>
            <tr><td>Potassium</td><td>mg</td><td>640</td><td>160</td></tr>
            <tr><td>Chloride</td><td>mg</td><td>175</td><td>43.8</td></tr>
            <tr class="group"><td colspan="4">11 Essential Vitamins</td></tr>
            <tr><td>Vitamin A</td><td>IU</td><td>1600</td><td>400</td></tr>
            <tr><td>Vitamin D</td><td>IU</td><td>360</td><td>90</td></tr>
            <tr><td>Vitamin C</td><td>mg</td><td>80</td><td>20</td></tr>
            <tr><td>Thiamine B1</td><td>mg</td><td>2</td><td>0.5</td></tr>
            <tr><td>Riboflavin B2</td><td>mg</td><td>2</td><td>0.5</td></tr>
            <tr><td>Vitamin B6</td><td>mg</td><td>4</td><td>1</td></tr>
            <tr><td>Vitamin B12</td><td>mcg</td><td>2.6</td><td>0.65</td></tr>
            <tr><td>Folic Acid</td><td>mcg</td><td>120</td><td>30</td></tr>
            <tr><td>Niacin</td><td>mg</td><td>10</td><td>2.5</td></tr>
            <tr><td>d-Biotin</td><td>mcg</td><td>20</td><td>5</td></tr>
            <tr><td>Pantothenic Acid</td><td>mg</td><td>2.4</td><td>0.6</td></tr>
          </table>
        </div>
      </div>
      <div class="ingredients">
        <p><b>Ingredients :</b> Sucrose, Soy protein isolate, Corn syrup solids, Vegetable oil (Palm Oil), Dextrose, Beet root juice powder.</p>
        <p><b>Minerals :</b> Dicalcium Phosphate, Tri Sodium Citrate, Magnesium Oxide, Ferric Pyrophosphate, Copper Gluconate, Zinc Sulphate, Potassium Iodate.</p>
        <p><b>Vitamins :</b> Ascorbic Acid, Niacinamide, Vitamin A Acetate, Pyridoxine Hydrochloride, Ergocalciferol, Thiamine Hydrochloride, Calcium Pantothenate, Riboflavin, Cyanocobalamin, Folic Acid, d-Biotin.</p>
      </div>
      <p class="small-caps">CONTAINS PERMITTED NATURAL COLOUR AND ADDED ARTIFICIAL FLAVOURING SUBSTANCES<br>THIS PACKAGE IS SOLD BY WEIGHT, NOT BY VOLUME SIGNIFICANT PRODUCT SETTLING MAY OCCUR</p>
      <div class="maker">
        <p>Manufactured By : Meridan Health Formulations Ltd.<br><span style="font-size:7px">(An ISO 9001:2000 &amp; 22000:2005 &amp; GMP Certified Company)</span><br>Plot 12, Sunrise Industrial Estate, JAIPUR 302000 INDIA</p>
        <p class="note"><b>Note :</b> Use this product as a food supplement only.</p>
      </div>
      <p class="dist">To be sold by Authorised Kestrel Distributors only</p>
    </div>
  </section>

  <section class="panel panel-front">
    <svg class="front-art" viewBox="0 0 404 458" preserveAspectRatio="none" aria-hidden="true">
      <defs>
        <radialGradient id="glow" cx="50%" cy="45%" r="55%">
          <stop offset="0" stop-color="#f2f8e2"/>
          <stop offset="0.6" stop-color="#cfe49a"/>
          <stop offset="1" stop-color="#9bc23c"/>
        </radialGradient>
      </defs>
      <rect width="404" height="458" fill="#ffffff"/>
      <path d="M0 140 C120 160 260 150 404 60 L404 458 L0 458 Z" fill="#9bc23c"/>
      <path d="M0 150 C130 175 270 160 404 80 L404 458 L0 458 Z" fill="#b7d66a"/>
      <ellipse cx="205" cy="270" rx="205" ry="120" fill="url(#glow)"/>
      <path d="M30 160 C140 110 280 110 380 160" fill="none" stroke="#5c0e0e" stroke-width="3"/>
      <rect x="0" y="366" width="404" height="92" fill="#b27852"/>
    </svg>
    <div class="brand">Greenmere</div>
    <div class="tagline">Daily Nourishment Co.</div>
    <div class="product">Vita-Core</div>
    <div class="subtitle">Balanced Nutritional Supplement</div>
    <div class="splash" role="img" aria-label="Chocolate drink splash"></div>
    <div class="badge">
      <span>NUTRITIONALLY GOOD</span>
      <span class="badge-art-wrap"><span class="badge-art" role="img" aria-label="Cocoa pod"></span></span>
      <span>CHOCOLATE<br>FLAVOR</span>
    </div>
    <div class="weight">Nett Weight 200g</div>
  </section>

  <section class="panel panel-right">
    <div class="info-box">
      <h2 class="headline">WONDERFUL, DELIGHTFUL, FANTASTIC DELICIOUS,<br>CHOCOLATE FLAVOURED DRINK</h2>
      <div class="copy">
        <p>Vita-Core Chocolate is the scientifically formulated balanced nutritional supplement with the power of high quality Soy protein, essential amino acids and important minerals &amp; vitamins that fits today's busy life style.</p>
        <p>This product should be used by individuals who may not consume adequate amounts of milk, meat, cheese or other high protein foods, individuals who require additional protein like children, adolescents, athletes, elderly, pregnant &amp; lactating women.</p>
        <ul>
          <li>Be it breakfast time, at work/school, after play or at bedtime, Vita-Core is the ideal drink to supplement your diet and ensures good nutritional intake in the case of fussy eaters.</li>
          <li>Supplements your daily diet with Proteins, Carbohydrates, Vitamins &amp; Minerals.</li>
          <li>Lactose free and low fat formulation.</li>
          <li>Can be conveniently used with warm or cold milk/water.</li>
          <li>These important nutrients help your child grow up with strong bones and muscles, healthy teeth, hair and skin good vision, sharp mental skills and lots of energy.</li>
          <li>1-2 glasses of Vita-Core drink everyday provides nourishment, strength, stamina &amp; immunity.</li>
          <li>Vita-Core Chocolate is a healthy alternative to unhealthy snacks like colas, pizzas, burgers, noodles, sweets, candies and other junk foods.</li>
        </ul>
        <p>**Protein Digestibility Corrected Amino Acid Score (PDCAAS) is a global standard established by the W.H.O. with a score of 1.0 representing the highest possible score for a quality protein source.</p>
      </div>
      <div class="protein">
        <b>Protein requirement /day :</b> Our protein needs depend on our age, size, and activity level. ICMR recommends the following protein intake for different life stages for Indian population.<br>
        <b>Adults</b> : 1g/Kg body weight/day. &nbsp;<b>Children</b> : 1.5g/Kg body weight/day.<br>
        <b>Pregnant/Lactating women</b> : 1.75 g/Kg body weight/day.
      </div>
      <p class="pdcaas">PDCAAS- **Protein Digestibility Corrected Amino Acid Score (PDCAAS) is a global standard established by the W.H.O. with a score of 1.0 representing the highest score possible for a quality protein source.</p>
      <div class="foot">
        <div class="storage">
          <strong>KEEP CONTAINER TIGHTLY CLOSED.<br>STORE IN A COOL &amp; DRY PLACE</strong>
          This Package is sold by weight, not by volume.<br>Significant product settling may occur.
          <span class="best">BEST BEFORE 24 MONTHS FROM PACKAGING.</span>
          <span class="fine">For Mfg. Lic. No., Batch No., Packaging Date, M.R.P. (Inclusive of All Taxes) See Bottom</span>
        </div>
        <div class="marketer">
          Marketed By :
          <div class="m-name"><span class="m-dot"></span>Kestrel</div>
          Marketed By : <b>Kestrel Retail Pvt. Ltd.</b><br>Unit 4, Lake View Complex,<br>Sector-9 Market, New Delhi-110000<br>Customer Care No. : 09800000000/10
        </div>
      </div>
    </div>
  </section>

</div>
</body>
</html>
```